Tandem Cove Digital Advertisement

This project is a request for a unique ad picture and message for Tandem Cove that will grab the audience instantly. Tandem Cove is a turn-around specialist and mobile online marketing agency. We create sustainable digital beach-heads (brand + value prop). Our tagline = Digital Builders. Our website is located at: tandemcove.example

Target Market(s)

small and medium business owners and leadership team

Requirements
Must have
• Key Messages: 1) TAP INTO THE RIGHT TRAFFIC 2) "Instinct is Correct. 7 out of 10 CEOs believe they're wasting advertising & marketing money" (Quillet) 3) Tandem Cove uses a proven and trademarked algorithm for growth.

```html
<!DOCTYPE html>
<html lang="en">
<head>
<meta charset="utf-8">
<title>Tandem Cove — Digital Builders</title>
<link rel="stylesheet" href="https://fonts.googleapis.com/css2?family=Antonio:wght@300;400&family=Montserrat:wght@400;500;600&display=swap">
<style>
  :root {
    --ink-dark: #1a1412;
    --ink-deep: #0f0b0a;
    --skin-warm: #5a4236;
    --skin-soft: #3a2a23;
    --brand-purple: #a15aa5;
    --brand-teal: #7fc0c6;
    --text-light: #ffffff;
    --text-muted: #e6dcd6;
    --text-dark: #111111;
    --footer-bg: #ffffff;
    --rule: #111111;
    --mark-frame: #8a8a8a;
  }
  * { margin: 0; padding: 0; box-sizing: border-box; }
  html, body { width: 848px; height: 1200px; overflow: hidden; background: var(--ink-dark); }
  .poster { position: relative; width: 848px; height: 1200px; overflow: hidden; }

  .hero {
    position: absolute; left: 0; top: 0; width: 848px; height: 1045px;
    background:
      radial-gradient(ellipse 300px 150px at 430px 570px, var(--skin-warm) 0%, var(--skin-soft) 45%, transparent 100%),
      radial-gradient(ellipse 420px 260px at 520px 590px, #2a201c 0%, transparent 100%),
      linear-gradient(180deg, var(--ink-deep) 0%, var(--ink-dark) 60%, #1c1613 100%);
  }

  .intro {
    position: absolute; top: 72px; left: 0; width: 848px;
    text-align: center; color: var(--text-light);
    font-family: "Montserrat", sans-serif; font-weight: 500;
    font-size: 23px; line-height: 31px;
  }

  .wordmark {
    position: absolute; left: 0; width: 848px; text-align: center;
    font-family: "Antonio", sans-serif; font-weight: 300;
    text-transform: uppercase; line-height: 1;
  }
  .wordmark--top { top: 217px; font-size: 192px; letter-spacing: 8px; color: var(--brand-purple); }
  .wordmark--bottom { top: 698px; font-size: 231px; letter-spacing: 12px; color: var(--brand-teal); }

  .messages {
    position: absolute; left: 0; top: 452px; width: 848px; text-align: center;
    font-family: "Montserrat", sans-serif; color: var(--text-light);
  }
  .messages__headline {
    font-size: 26px; font-weight: 600; letter-spacing: 3px; line-height: 32px;
  }
  .messages__stat {
    margin: 120px auto 0; width: 620px;
    font-size: 17px; font-weight: 500; line-height: 24px; color: var(--text-muted);
  }
  .messages__source { font-weight: 400; }
  .messages__claim {
    margin-top: 12px; font-size: 17px; font-weight: 500; line-height: 24px; color: var(--brand-teal);
  }

  .tagline {
    position: absolute; top: 993px; left: 0; width: 848px; text-align: center;
    color: var(--text-light); font-family: "Montserrat", sans-serif; font-weight: 500;
    font-size: 24px; letter-spacing: 4px;
  }

  .footer {
    position: absolute; left: 0; top: 1045px; width: 848px; height: 155px;
    background: var(--footer-bg);
  }
  .footer__block {
    position: absolute; top: 48px; text-align: center;
    font-family: "Montserrat", sans-serif; color: var(--text-dark);
    font-size: 17px; letter-spacing: 1.5px; line-height: 26px;
  }
  .footer__label { letter-spacing: 3px; font-size: 18px; }
  .footer__block--web { left: 0; width: 290px; }
  .footer__block--contact { left: 556px; width: 292px; }
  .footer__rule {
    position: absolute; top: 40px; width: 3px; height: 64px; background: var(--rule);
  }
  .footer__rule--left { left: 291px; }
  .footer__rule--right { left: 553px; }

  .brand-mark {
    position: absolute; left: 366px; top: 8px; width: 111px; height: 126px;
    border: 1px solid var(--mark-frame);
    display: flex; flex-direction: column; align-items: center; justify-content: center; gap: 12px;
  }
  .brand-mark__square { width: 44px; height: 44px; background: var(--brand-purple); }
  .brand-mark__name {
    font-family: "Montserrat", sans-serif; font-weight: 600; font-size: 14px;
    color: var(--text-dark); text-align: center; line-height: 17px; letter-spacing: 0.5px;
  }
</style>
</head>
<body>
<main class="poster">
  <div class="hero" role="img" aria-label="Dark photograph of two hands holding a smartphone, one finger tapping the glowing screen"></div>

  <p class="intro">We help entrepreneurs and independent business owners<br>establish their mobile online presence to improve, optimize<br>and then sustain their business performance</p>

  <h1>
    <span class="wordmark wordmark--top">Tandem</span>
    <span class="wordmark wordmark--bottom">Cove</span>
  </h1>

  <section class="messages">
    <h2 class="messages__headline">TAP INTO THE RIGHT TRAFFIC</h2>
    <p class="messages__stat">Instinct is Correct. 7 out of 10 CEOs believe they're wasting advertising &amp; marketing money <span class="messages__source">(Quillet)</span></p>
    <p class="messages__claim">Tandem Cove uses a proven and trademarked algorithm for growth.</p>
  </section>

  <p class="tagline">DIGITAL BUILDERS</p>

  <footer class="footer">
    <div class="footer__block footer__block--web">
      <div class="footer__label">WEBSITE</div>
      <div>www.tandemcove.example</div>
    </div>
    <span class="footer__rule footer__rule--left"></span>

    <div class="brand-mark">
      <span class="brand-mark__square"></span>
      <span class="brand-mark__name">TANDEM<br>COVE</span>
    </div>

    <span class="footer__rule footer__rule--right"></span>
    <div class="footer__block footer__block--contact">
      <div class="footer__label">CONTACT</div>
      <div>info@tandemcove.example</div>
    </div>
  </footer>
</main>
</body>
</html>
```